Social Media Overlay for Ormond Real Estate

We need an social media overlay that can be added to a photo of a house that includes our current logo and a call to action of "Just Listed". This needs to be something that we can use for every new house that we list. Attached is our current logo in both company colors, purple and white. An example of a overlay from Plazeo that we like.

Target Market(s)

Social Media Real Estate Community - Real Estate Agents, Brokers, Buyers & Sellers

Industry/Entity Type

Real Estate

Font styles to use
Sans Serif

Colors
6c459b

Requirements
Must have
• the company colors, purple and white and the company logo
Nice to have
• call to action "Just Listed"
• some layered, texture, or 3-D effect
Should not have
• Should be clean and simple; nothing too busy

```html
<!DOCTYPE html>
<html lang="en">
<head>
<meta charset="utf-8">
<title>Ormond Real Estate – Just Listed Overlay</title>
<link rel="stylesheet" href="https://fonts.googleapis.com/css2?family=Bebas+Neue&family=Questrial&display=swap">
<style>
  :root {
    --brand-purple: #6c459b;
    --brand-white: #ffffff;
    --sky-top: #3a5a86;
    --sky-low: #7d93ad;
    --house-warm: #8a7a64;
    --lawn: #4f7a32;
    --shadow: rgba(0, 0, 0, 0.35);
  }
  html, body {
    margin: 0;
    padding: 0;
    overflow: hidden;
    background: var(--brand-white);
  }
  .canvas {
    position: relative;
    width: 1186px;
    height: 1200px;
    overflow: hidden;
    background: var(--brand-white);
  }
  .listing-photo {
    position: absolute;
    left: 0;
    top: 0;
    width: 1186px;
    height: 784px;
    background: linear-gradient(180deg,
      var(--sky-top) 0%,
      var(--sky-low) 30%,
      var(--house-warm) 55%,
      #6e5c48 72%,
      var(--lawn) 88%,
      #5d8a3a 100%);
  }
  .photo-logo {
    position: absolute;
    left: 8px;
    top: 8px;
    color: var(--brand-white);
    font-family: "Questrial", sans-serif;
    font-weight: 400;
    line-height: 1;
  }
  .photo-logo .name {
    display: block;
    font-size: 70px;
    letter-spacing: -1px;
  }
  .photo-logo .sub {
    display: block;
    font-size: 36px;
    margin-top: 6px;
    margin-left: 6px;
  }
  .sign-sheet {
    position: absolute;
    left: 0;
    top: 784px;
  }
  .sign { filter: drop-shadow(8px 8px 6px var(--shadow)); }
  .fill-purple { fill: var(--brand-purple); }
  .fill-white { fill: var(--brand-white); }
  .badge-name { font-family: "Questrial", sans-serif; font-size: 28px; }
  .badge-sub { font-family: "Questrial", sans-serif; font-size: 16px; }
  .badge-name-small { font-family: "Questrial", sans-serif; font-size: 21px; }
  .badge-sub-small { font-family: "Questrial", sans-serif; font-size: 12px; }
  .cta { font-family: "Bebas Neue", sans-serif; font-size: 80px; }
</style>
</head>
<body>
<main class="canvas">
  <div class="listing-photo" role="img" aria-label="Photo of a large two-storey house at dusk with lit windows, stone facade, garages and landscaped lawn"></div>
  <div class="photo-logo">
    <span class="name">Ormond</span>
    <span class="sub">Real Estate</span>
  </div>

  <svg class="sign-sheet" width="1186" height="416" viewBox="0 784 1186 416" aria-label="Just Listed sign variations">
    <g class="sign">
      <rect class="fill-white" x="230" y="833" width="328" height="126" rx="63"/>
      <rect class="fill-purple" x="236" y="841" width="314" height="110" rx="55"/>
      <rect class="fill-white" x="244" y="850" width="297" height="92" rx="46"/>
      <circle class="fill-white" cx="193" cy="897" r="79"/>
      <circle class="fill-purple" cx="193" cy="897" r="70"/>
      <text class="badge-name fill-white" x="193" y="900" text-anchor="middle" textLength="112" lengthAdjust="spacingAndGlyphs">Ormond</text>
      <text class="badge-sub fill-white" x="193" y="923" text-anchor="middle">Real Estate</text>
      <text class="cta fill-purple" x="282" y="925" textLength="243" lengthAdjust="spacingAndGlyphs">JUST LISTED</text>
    </g>

    <g class="sign">
      <path class="fill-white" d="M700 837 H1020 L1092 897 L1020 957 H700 Z"/>
      <path class="fill-purple" d="M700 845 H1014 L1080 897 L1014 949 H700 Z"/>
      <path class="fill-white" d="M700 854 H1008 L1064 897 L1008 940 H700 Z"/>
      <circle class="fill-white" cx="700" cy="897" r="79"/>
      <circle class="fill-purple" cx="700" cy="897" r="70"/>
      <text class="badge-name fill-white" x="700" y="900" text-anchor="middle" textLength="112" lengthAdjust="spacingAndGlyphs">Ormond</text>
      <text class="badge-sub fill-white" x="700" y="923" text-anchor="middle">Real Estate</text>
      <text class="cta fill-purple" x="788" y="922" textLength="214" lengthAdjust="spacingAndGlyphs">JUST LISTED</text>
    </g>

    <g class="sign">
      <rect class="fill-white" x="230" y="1017" width="336" height="132" rx="66"/>
      <rect class="fill-purple" x="238" y="1027" width="318" height="112" rx="56"/>
      <circle class="fill-white" cx="191" cy="1084" r="82"/>
      <circle class="fill-purple" cx="191" cy="1084" r="70"/>
      <circle class="fill-white" cx="191" cy="1084" r="57"/>
      <text class="badge-name-small fill-purple" x="191" y="1086" text-anchor="middle" textLength="86" lengthAdjust="spacingAndGlyphs">Ormond</text>
      <text class="badge-sub-small fill-purple" x="191" y="1102" text-anchor="middle">Real Estate</text>
      <text class="cta fill-white" x="284" y="1116" textLength="246" lengthAdjust="spacingAndGlyphs">JUST LISTED</text>
    </g>

    <g class="sign">
      <path class="fill-white" d="M700 1018 H1010 L1088 1082 L1010 1146 H700 Z"/>
      <path class="fill-purple" d="M700 1027 H1005 L1074 1082 L1005 1137 H700 Z"/>
      <circle class="fill-white" cx="702" cy="1084" r="82"/>
      <circle class="fill-purple" cx="702" cy="1084" r="70"/>
      <circle class="fill-white" cx="702" cy="1084" r="57"/>
      <text class="badge-name-small fill-purple" x="702" y="1084" text-anchor="middle" textLength="86" lengthAdjust="spacingAndGlyphs">Ormond</text>
      <text class="badge-sub-small fill-purple" x="702" y="1100" text-anchor="middle">Real Estate</text>
      <text class="cta fill-white" x="794" y="1113" textLength="210" lengthAdjust="spacingAndGlyphs">JUST LISTED</text>
    </g>
  </svg>
</main>
</body>
</html>
```